Web Design for historic veg friendly, organic restaurant

We need a new web site. The Brookmere Cafe is a 40 year old restaurant in Chicago. We've been one of the premier, casual vegetarian restaurants since we opened. 5 years ago, Brookmere Cafe was purchased from the original owners by a local, certified organic farmer. We are nearly 100% from scratch kitchen, 100% certified organic produce, we are governed by a strict sustainable plan and we are very active politically. But you wouldn't know it form our website! We have a desire to build a simple website around some basic principles:
1. We need our current logo prominently displayed (logo attached)
2. We need a "click to call" easily accessible
3. We have an online order link that needs to be easily accessible
4. We need our hours, location, and directions easy to see
4. We need a separate events page (we have a live music and events venue that runs shows 5-7 nights per week.)
5. We would like to have a separate page for pictures, particularly old pictures. It would be fun to have a function for people to post their own shots, but that might make this too complicated. If it were possible, we would of course need to retain the ability to curate posted pictures.
6. This needs to be easily edited by us, so in a platform such as word press or similar
7. We will need this mobile enhanced

Target Market(s)

Neighborhood residents - zip code is 60626

Industry/Entity Type

Restaurant

Coding

Coded - Design and coding required

Number of Pages Required

4 page

Font styles to use
Sans Serif

Requirements
Must have
• Logo, click to call, events page that we can manage, contact us, about us page, menu (we have the online menu through a third party plugin), a page for our market and some nice pictures on our splash page,
• Must be mobile ready and on a platform such as Word Press or some other platform where we can edit on our own
Nice to have
• Page for past employees and historical pictures, be nice to have food pictures or something similar on a scroll, would love to have an ability for others to post pictures that we would "approve"
Should not have
• We don't need anything that spins, moves, flames or other features that detract from gathering information

```html
<!DOCTYPE html>
<html lang="en">
<head>
<meta charset="utf-8">
<title>Brookmere Cafe</title>
<link rel="stylesheet" href="https://fonts.googleapis.com/css2?family=Nunito:wght@300;400;600;700;800&family=Open+Sans:wght@400;600&display=swap">
<style>
:root{
  --black:#000;
  --footer:#1c1c1c;
  --yellow:#f7df3a;
  --red:#e0221f;
  --dark-text:#222;
  --white:#fff;
  --wood-dark:#6e5140;
  --wood-mid:#8d6b55;
  --pink:#d18c9b;
  --lavender:#b9a3cb;
}
*{box-sizing:border-box;margin:0;padding:0}
html,body{width:1200px;height:2761px;overflow:hidden;background:var(--white)}
body{position:relative;font-family:"Open Sans",Arial,sans-serif;color:var(--dark-text)}
h1,h2,h3,h4{font-weight:400}
.abs{position:absolute}

/* header */
.site-header{left:0;top:0;width:1200px;height:107px;background:var(--black)}
.brand{left:114px;top:24px;width:240px;height:70px;display:flex;align-items:center;gap:10px;z-index:3}
.brand-dot{width:20px;height:20px;border-radius:50%;background:var(--red);flex:none}
.brand-name{font-family:"Nunito",sans-serif;font-weight:800;font-size:30px;line-height:32px;color:var(--red)}
.btn-order{left:745px;top:42px;width:162px;height:45px;border-radius:23px;background:var(--yellow);color:#111;font-family:"Nunito",sans-serif;font-weight:700;font-size:17px;display:flex;align-items:center;justify-content:center}
.btn-call{left:922px;top:42px;width:166px;height:45px;border-radius:23px;background:var(--red);color:var(--white);font-family:"Nunito",sans-serif;font-weight:600;font-size:16px;display:flex;align-items:center;justify-content:center;gap:6px}
.main-nav{left:0;top:107px;width:1200px;height:55px;background:var(--yellow)}
.main-nav ul{position:absolute;left:377px;top:0;height:55px;display:flex;list-style:none}
.main-nav li{height:55px;display:flex;align-items:center;padding:0 15px;font-family:"Nunito",sans-serif;font-weight:600;font-size:15.5px;color:#111;border-left:1px solid #c9b22a}
.main-nav li:first-child{border-left:none}

/* hero */
.hero{left:0;top:162px;width:1200px;height:998px;overflow:hidden}
.hero-photo{left:0;top:0;width:1200px;height:998px;background:linear-gradient(135deg,var(--wood-dark),var(--wood-mid) 45%,#5b4132)}
.hero-lower{left:0;top:0;width:1200px;height:998px}
.slide-arrow{width:52px;height:52px;border-radius:50%;border:2px solid var(--white);display:flex;align-items:center;justify-content:center}
.slide-kicker{left:0;top:200px;width:1200px;text-align:center;font-family:"Nunito",sans-serif;font-weight:300;font-size:31px;color:var(--white)}
.slide-title{left:0;top:240px;width:1200px;text-align:center;font-family:"Nunito",sans-serif;font-weight:600;font-size:44px;line-height:50px;color:var(--white)}
.intro-title{left:0;top:645px;width:1200px;text-align:center;font-family:"Nunito",sans-serif;font-weight:400;font-size:38px;color:var(--dark-text)}
.intro-title span{color:var(--red)}
.intro-text{left:262px;top:718px;width:676px;text-align:center;font-size:15px;line-height:29px;color:#8a8580}
.btn-more{left:517px;top:868px;width:166px;height:46px;border-radius:23px;background:var(--black);color:var(--white);font-family:"Nunito",sans-serif;font-weight:600;font-size:16px;display:flex;align-items:center;justify-content:center}

/* feature band */
.feature-band{left:0;top:1160px;width:1200px;height:469px;background:linear-gradient(90deg,var(--lavender),var(--pink) 30%,#d593a2 50%,var(--pink) 70%,var(--lavender))}
.feature{width:294px;height:294px;top:1255px}
.feature svg{position:absolute;left:0;top:0}
.feature-label{position:absolute;left:0;top:184px;width:294px;text-align:center;font-family:"Nunito",sans-serif;font-weight:600;font-size:27px;color:var(--white)}

/* events */
.section-title{left:0;top:1668px;width:1200px;text-align:center;font-family:"Nunito",sans-serif;font-weight:400;font-size:38px;color:var(--red)}
.event{top:1745px;width:304px}
.event-photo{width:304px;height:226px}
.event-title{margin-top:16px;text-align:center;font-family:"Nunito",sans-serif;font-weight:400;font-size:24px;color:#111}
.event-rule{width:56px;height:3px;background:var(--red);margin:4px auto 12px}
.event-text{text-align:center;font-size:12px;line-height:18px;color:#777;padding:0 14px}
.event-link{margin-top:6px;text-align:center;font-size:13px;color:var(--red)}

/* newsletter */
.newsletter{left:0;top:2190px;width:1200px;height:105px;background:var(--yellow)}
.newsletter-label{left:202px;top:36px;font-family:"Nunito",sans-serif;font-size:24px;color:#111}
.newsletter-input{left:442px;top:35px;width:429px;height:41px;border:1px solid #6d6423;font-size:13px;color:#222;padding-left:20px;display:flex;align-items:center}
.newsletter-btn{left:876px;top:35px;width:125px;height:41px;background:var(--red);color:var(--white);font-family:"Nunito",sans-serif;font-size:17px;display:flex;align-items:center;justify-content:center}

/* footer */
.site-footer{left:0;top:2295px;width:1200px;height:466px;background:var(--footer);color:var(--white)}
.footer-heading{top:55px;font-family:"Nunito",sans-serif;font-weight:400;font-size:22px;letter-spacing:.3px}
.footer-text{font-size:13.5px;line-height:24px}
.contact-line{display:flex;gap:12px;align-items:flex-start;font-size:13.5px;line-height:20px;margin-bottom:12px}
.contact-line svg{flex:none;margin-top:2px}
.social{display:flex;gap:8px}
.social span{width:34px;height:34px;border:2px solid var(--yellow);border-radius:50%}
.map{left:769px;top:99px;width:285px;height:178px;background:linear-gradient(135deg,#e3e7da,#d3dbe6 55%,#9ec0e6)}
.footer-rule{left:133px;top:342px;width:944px;height:1px;background:#3a3a3a}
.footer-nav{left:133px;top:374px;display:flex;gap:26px;list-style:none;font-size:13px;color:#9a9a9a}
.copyright{left:133px;top:406px;font-size:12.5px;color:#8a8a8a}
</style>
</head>
<body>

<header class="site-header abs"></header>
<div class="brand abs"><span class="brand-dot"></span><span class="brand-name">Brookmere<br>Cafe</span></div>
<div class="btn-order abs">Online Order</div>
<div class="btn-call abs">
  <svg width="18" height="18" viewBox="0 0 24 24" fill="none" stroke="#fff" stroke-width="2"><path d="M5 3h4l2 5-2.5 1.5a11 11 0 0 0 6 6L16 13l5 2v4a2 2 0 0 1-2 2A16 16 0 0 1 3 5a2 2 0 0 1 2-2z"/></svg>
  CLICK TO CALL
</div>
<nav class="main-nav abs">
  <ul>
    <li>HOME</li><li>ABOUT</li><li>LOCATION &amp; HOURS</li><li>EVENTS</li><li>BOOKING</li><li>BLOG</li><li>CONTACT US</li>
  </ul>
</nav>

<section class="hero abs">
  <div class="hero-photo abs" role="img" aria-label="Plate of grilled kofta on lettuce over a rustic wooden table"></div>
  <svg class="hero-lower abs" width="1200" height="998" viewBox="0 0 1200 998">
    <defs>
      <linearGradient id="tableLight" x1="0" y1="0" x2="0" y2="1">
        <stop offset="0" stop-color="#f1eae0"/>
        <stop offset="1" stop-color="#e4d6c3"/>
      </linearGradient>
    </defs>
    <path d="M0 540 C220 520 420 560 620 545 C820 530 1000 420 1200 390 L1200 998 L0 998 Z" fill="var(--red)"/>
    <path d="M0 574 C220 555 420 580 620 565 C820 548 1000 470 1200 452 L1200 998 L0 998 Z" fill="url(#tableLight)" role="img" aria-label="Breakfast spread of eggs, pasta, bread and coffee on a light table"/>
  </svg>
  <div class="slide-arrow abs" style="left:98px;top:226px">
    <svg width="16" height="16" viewBox="0 0 16 16" fill="none" stroke="#fff" stroke-width="2"><path d="M10 2 4 8l6 6"/></svg>
  </div>
  <div class="slide-arrow abs" style="left:1048px;top:226px">
    <svg width="16" height="16" viewBox="0 0 16 16" fill="none" stroke="#fff" stroke-width="2"><path d="m6 2 6 6-6 6"/></svg>
  </div>
  <p class="slide-kicker abs">Welcome to the Brookmere Cafe</p>
  <h1 class="slide-title abs">Good Wholesome Food for the Mind<br>&amp; Body in Lindell Grove</h1>
  <h2 class="intro-title abs">Welcome to <span>Brookmere Cafe</span></h2>
  <p class="intro-text abs">Fusce ultricies orci ac feugiat suscipit leo massa sodales velit et scelerisque mi tortor at ipsum cligula augue bibendum accumsan vestibulum ut commodo a mi Morbi ornare gravida elit Integer congue augue et maecenas iaculis ipsum dui aliquet felis at cursus magna nisl nec elit Praesent</p>
  <div class="btn-more abs">Learn More</div>
</section>

<section class="feature-band abs" role="img" aria-label="Pink and lavender sunburst backdrop"></section>

<div class="feature abs" style="left:125px">
  <svg width="294" height="294" viewBox="0 0 294 294">
    <path d="M265 147A40 40 0 0 1 242.5 216.4A40 40 0 0 1 183.5 259.2A40 40 0 0 1 110.5 259.2A40 40 0 0 1 51.5 216.4A40 40 0 0 1 29 147A40 40 0 0 1 51.5 77.6A40 40 0 0 1 110.5 34.8A40 40 0 0 1 183.5 34.8A40 40 0 0 1 242.5 77.6A40 40 0 0 1 265 147Z" fill="none" stroke="#fff" stroke-width="3"/>
    <path d="M251 147A34 34 0 0 1 231.1 208.2A34 34 0 0 1 179.1 245.9A34 34 0 0 1 114.9 245.9A34 34 0 0 1 62.9 208.2A34 34 0 0 1 43 147A34 34 0 0 1 62.9 85.8A34 34 0 0 1 114.9 48.1A34 34 0 0 1 179.1 48.1A34 34 0 0 1 231.1 85.8A34 34 0 0 1 251 147Z" fill="#3a2a24" role="img" aria-label="Breakfast plate with fried egg and toast"/>
    <path d="M118 126a29 29 0 0 1 58 0z" fill="none" stroke="#fff" stroke-width="5"/>
    <rect x="110" y="128" width="74" height="6" rx="2" fill="#fff"/>
    <circle cx="147" cy="91" r="5" fill="#fff"/>
    <line x1="94" y1="223" x2="200" y2="223" stroke="#fff" stroke-width="2"/>
  </svg>
  <div class="feature-label">Menu</div>
</div>
<div class="feature abs" style="left:445px">
  <svg width="294" height="294" viewBox="0 0 294 294">
    <path d="M265 147A40 40 0 0 1 242.5 216.4A40 40 0 0 1 183.5 259.2A40 40 0 0 1 110.5 259.2A40 40 0 0 1 51.5 216.4A40 40 0 0 1 29 147A40 40 0 0 1 51.5 77.6A40 40 0 0 1 110.5 34.8A40 40 0 0 1 183.5 34.8A40 40 0 0 1 242.5 77.6A40 40 0 0 1 265 147Z" fill="none" stroke="#fff" stroke-width="3"/>
    <path d="M251 147A34 34 0 0 1 231.1 208.2A34 34 0 0 1 179.1 245.9A34 34 0 0 1 114.9 245.9A34 34 0 0 1 62.9 208.2A34 34 0 0 1 43 147A34 34 0 0 1 62.9 85.8A34 34 0 0 1 114.9 48.1A34 34 0 0 1 179.1 48.1A34 34 0 0 1 231.1 85.8A34 34 0 0 1 251 147Z" fill="#4a2a3e" role="img" aria-label="Guitarist performing on a dim stage"/>
    <path d="M134 90v50M168 82v50M134 90l34-8M134 98l34-8" stroke="#fff" stroke-width="5" fill="none"/>
    <ellipse cx="125" cy="141" rx="11" ry="8" fill="#fff"/>
    <ellipse cx="159" cy="133" rx="11" ry="8" fill="#fff"/>
    <line x1="94" y1="223" x2="200" y2="223" stroke="#fff" stroke-width="2"/>
  </svg>
  <div class="feature-label">Music</div>
</div>
<div class="feature abs" style="left:766px">
  <svg width="294" height="294" viewBox="0 0 294 294">
    <path d="M265 147A40 40 0 0 1 242.5 216.4A40 40 0 0 1 183.5 259.2A40 40 0 0 1 110.5 259.2A40 40 0 0 1 51.5 216.4A40 40 0 0 1 29 147A40 40 0 0 1 51.5 77.6A40 40 0 0 1 110.5 34.8A40 40 0 0 1 183.5 34.8A40 40 0 0 1 242.5 77.6A40 40 0 0 1 265 147Z" fill="none" stroke="#fff" stroke-width="3"/>
    <path d="M251 147A34 34 0 0 1 231.1 208.2A34 34 0 0 1 179.1 245.9A34 34 0 0 1 114.9 245.9A34 34 0 0 1 62.9 208.2A34 34 0 0 1 43 147A34 34 0 0 1 62.9 85.8A34 34 0 0 1 114.9 48.1A34 34 0 0 1 179.1 48.1A34 34 0 0 1 231.1 85.8A34 34 0 0 1 251 147Z" fill="#4e5a3a" role="img" aria-label="Farm field with trees at sunset"/>
    <path d="M118 146V106l29-26 29 26v40z" fill="none" stroke="#fff" stroke-width="5"/>
    <rect x="133" y="115" width="28" height="28" fill="none" stroke="#fff" stroke-width="4"/>
    <path d="M133 115l28 28M161 115l-28 28" stroke="#fff" stroke-width="3"/>
    <line x1="94" y1="223" x2="200" y2="223" stroke="#fff" stroke-width="2"/>
  </svg>
  <div class="feature-label">Farm</div>
</div>

<h2 class="section-title abs">Our Events</h2>
<article class="event abs" style="left:118px">
  <div class="event-photo" role="img" aria-label="Glasses of red wine raised in a toast" style="background:linear-gradient(135deg,#5a1a1e,#b8474a 55%,#3a1518)"></div>
  <h3 class="event-title">Event Tittle here</h3>
  <div class="event-rule"></div>
  <p class="event-text">sociosqu ad litora torquent per conubia nostra per inceptos hymenaeos Proin nulla arcu nonummy luctus dictum eget</p>
  <p class="event-link">READ MORE</p>
</article>
<article class="event abs" style="left:447px">
  <div class="event-photo" role="img" aria-label="Friends sharing a meal at a dinner table" style="background:linear-gradient(135deg,#3e2e26,#9a7a66 55%,#d8c7b7)"></div>
  <h3 class="event-title">Event Tittle here</h3>
  <div class="event-rule"></div>
  <p class="event-text">sociosqu ad litora torquent per conubia nostra per inceptos hymenaeos Proin nulla arcu nonummy luctus dictum eget</p>
  <p class="event-link">READ MORE</p>
</article>
<article class="event abs" style="left:777px">
  <div class="event-photo" role="img" aria-label="Overhead view of a table full of shared dishes" style="background:linear-gradient(135deg,#4a3a2e,#7d6a4a 50%,#3a4a3a)"></div>
  <h3 class="event-title">Event Tittle here</h3>
  <div class="event-rule"></div>
  <p class="event-text">sociosqu ad litora torquent per conubia nostra per inceptos hymenaeos Proin nulla arcu nonummy luctus dictum eget</p>
  <p class="event-link">READ MORE</p>
</article>

<section class="newsletter abs">
  <div class="newsletter-label abs">Newsletter Sign Up</div>
  <div class="newsletter-input abs">EMAIL ADDRESS</div>
  <div class="newsletter-btn abs">Subscribe</div>
</section>

<footer class="site-footer abs">
  <h4 class="footer-heading abs" style="left:133px">OUR HOURS</h4>
  <div class="abs footer-text" style="left:133px;top:105px">Monday-Friday: 8am to 10pm<br>Sat-Sunday: 9am to 11pm</div>
  <div class="abs" style="left:133px;top:173px;font-size:12.5px;line-height:22px">Delivery is Available from 12 pm<br>to 10 pm, 7 days per week</div>

  <h4 class="footer-heading abs" style="left:449px">LOCATIONS</h4>
  <div class="abs" style="left:449px;top:105px;width:270px">
    <div class="contact-line">
      <svg width="14" height="18" viewBox="0 0 14 18"><path d="M7 0a7 7 0 0 0-7 7c0 5 7 11 7 11s7-6 7-11a7 7 0 0 0-7-7z" fill="var(--yellow)"/><circle cx="7" cy="7" r="2.6" fill="var(--footer)"/></svg>
      <span>482 N Lindell Avenue, Suite 3<br>Ashford 40117</span>
    </div>
    <div class="contact-line">
      <svg width="16" height="16" viewBox="0 0 24 24"><path d="M5 3h4l2 5-2.5 1.5a11 11 0 0 0 6 6L16 13l5 2v4a2 2 0 0 1-2 2A16 16 0 0 1 3 5a2 2 0 0 1 2-2z" fill="var(--yellow)"/></svg>
      <span>555-018-2247</span>
    </div>
    <div class="contact-line">
      <svg width="18" height="14" viewBox="0 0 18 14"><rect width="18" height="14" rx="1" fill="var(--yellow)"/><path d="M1 1l8 6 8-6" stroke="var(--footer)" stroke-width="1.6" fill="none"/></svg>
      <span>hello@brookmerecafe.example</span>
    </div>
    <div class="social" style="margin-top:6px"><span></span><span></span><span></span><span></span><span></span></div>
  </div>

  <h4 class="footer-heading abs" style="left:766px">OUR DIRECTIONS</h4>
  <div class="map abs" role="img" aria-label="Street map showing the cafe location"></div>

  <div class="footer-rule abs"></div>
  <ul class="footer-nav abs">
    <li>HOME</li><li>ABOUT</li><li>LOCATION &amp; HOURS</li><li>EVENTS</li><li>BOOKING</li><li>BLOG</li><li>CONTACT US</li>
  </ul>
  <p class="copyright abs">© 2017 Company Name &nbsp;All right reserved &nbsp;Term of Use</p>
</footer>

</body>
</html>
```